Letterhead Design Project

I am the new owner of an existing Accouting and Financial Planning Firm (which I have been an employee at for 3 years)
We need to change the letterhead due to a change to the company's ABN etc., so thought we would like to modernise this at the same time.
We wish to keep the existing logo so there is familiarity to the clients. As per the notes on the attached document, we are happy to remove the wording from the logo, whichever will look better.
The letterhead needs to be professional, yet modern.
I will upload our logo and the required details for the letterhead.

Industry/Entity Type

Financial

Requirements
Must have
• Logo and provided business details.

```html
<!DOCTYPE html>
<html lang="en">
<head>
<meta charset="utf-8">
<title>Kelbrook Accountants – Letterhead</title>
<link href="https://fonts.googleapis.com/css2?family=Open+Sans:wght@400;700&display=swap" rel="stylesheet">
<style>
  :root {
    --navy: #1d3f7f;
    --orange: #e49b16;
    --paper: #ffffff;
    --stage: #ffffff;
    --edge: #3a3a3a;
    --mist: #d9e0ea;
    --cream: #fbeed8;
  }
  html, body {
    margin: 0;
    padding: 0;
    width: 1200px;
    height: 900px;
    overflow: hidden;
    background: var(--stage);
    font-family: "Open Sans", Arial, sans-serif;
    color: var(--navy);
  }
  .canvas {
    position: relative;
    width: 1200px;
    height: 900px;
  }
  .sheet {
    position: absolute;
    top: 62px;
    width: 527px;
    height: 745px;
    background: var(--paper);
    border: 1px solid var(--edge);
    box-sizing: border-box;
    overflow: hidden;
  }
  .sheet--first { left: 47px; }
  .sheet--follow { left: 620px; }

  .watermark {
    position: absolute;
    left: -40px;
    top: 170px;
    width: 610px;
    height: 480px;
    pointer-events: none;
  }
  .watermark__dot {
    position: absolute;
    left: 150px;
    top: 150px;
    width: 170px;
    height: 170px;
    border-radius: 50%;
    background: var(--cream);
  }
  .watermark__name {
    position: absolute;
    left: 40px;
    top: 185px;
    margin: 0;
    font-size: 96px;
    font-weight: 700;
    letter-spacing: 2px;
    line-height: 1;
    color: var(--mist);
    transform: rotate(-28deg);
    transform-origin: center;
    white-space: nowrap;
  }

  .brand-mark {
    position: absolute;
    top: 48px;
    margin: 0;
    font-size: 26px;
    font-weight: 700;
    letter-spacing: 1px;
    color: var(--navy);
    line-height: 1;
  }
  .sheet--first .brand-mark { left: 52px; }
  .sheet--follow .brand-mark { right: 52px; }

  .brand-title {
    position: absolute;
    top: 37px;
    right: 32px;
    margin: 0;
    text-align: right;
    font-size: 13.5px;
    font-weight: 400;
    line-height: 17.5px;
    letter-spacing: 0.2px;
    color: var(--navy);
  }
  .brand-title__square {
    position: absolute;
    top: 42px;
    right: 151px;
    width: 13px;
    height: 13px;
    background: var(--orange);
  }

  .contact {
    position: absolute;
    margin: 0;
    font-style: normal;
    font-size: 10px;
    line-height: 13.6px;
    text-transform: uppercase;
    color: var(--navy);
    letter-spacing: 0.1px;
  }
  .contact--address { left: 27px; top: 677px; }
  .contact--numbers { right: 23px; top: 651px; text-align: right; }
  .sheet--follow .contact--address { left: 57px; top: 651px; }
</style>
</head>
<body>
<main class="canvas">

  <section class="sheet sheet--first" aria-label="Letterhead, first page">
    <div class="watermark" aria-hidden="true">
      <span class="watermark__dot"></span>
      <p class="watermark__name">KELBROOK</p>
    </div>

    <p class="brand-mark">KELBROOK</p>
    <span class="brand-title__square"></span>
    <h1 class="brand-title">KELBROOK<br>ACCOUNTANTS<br>&amp; FINANCIAL<br>SERVICES</h1>

    <address class="contact contact--address">
      Kelbrook Accountants &amp; Financial Services<br>
      18 Marlow Street, Riverton, VIC, 3620,<br>
      PO Box 4410, Eastvale, NSW, 2655
    </address>
    <address class="contact contact--numbers">
      ABN: 41 208 337 912<br>
      PH: 02 5550 1840<br>
      FAX: 02 5550 1841<br>
      Email: admin@kelbrookaccounts.com.au<br>
      www.kelbrookaccounts.com.au
    </address>
  </section>

  <section class="sheet sheet--follow" aria-label="Letterhead, following page">
    <div class="watermark" aria-hidden="true">
      <span class="watermark__dot"></span>
      <p class="watermark__name">KELBROOK</p>
    </div>

    <p class="brand-mark">KELBROOK</p>

    <address class="contact contact--address">
      Kelbrook Accountants &amp; Financial Services<br>
      18 Marlow Street, Riverton, VIC, 3620,<br>
      PO Box 4410, Eastvale, NSW, 2655
    </address>
    <address class="contact contact--numbers">
      ABN: 41 208 337 912<br>
      PH: 02 5550 1840<br>
      FAX: 02 5550 1841<br>
      Email: admin@kelbrookaccounts.com.au<br>
      www.kelbrookaccounts.com.au
    </address>
  </section>

</main>
</body>
</html>
```